Varnek Group Business Card

Varnek Group — Business Card Design Brief
Overview
Design a double-sided business card for Varnek Group that highlights our two service arms: Varnek Communications (telecommunications) and Varnek Energy (business energy solutions). The card should feel smart and stand out when handed to clients.

Objectives
Showcase our areas of specialty clearly.
Reflect the overall Varnek / Varnek Group brand while acknowledging both arms.
Explore using both logos (Communications + Energy) or one unified logo, depending on the design.

Deliverables
One double-sided business card design (front + back).

Content & Copy
Front (preferred): Logo: Varnek / Varnek Group
Descriptor: Business Communications | Business Energy
Back:My contact details and company details
Core products: Business Mobile • Telephony • Internet • Business Energy Solutions

Brand & Visual Direction
We have a group logo currently tailored more toward telecoms, plus a separate Varnek Energy logo.
Please explore layouts that use both logos or just one, whichever works best.
Color: I wouldn't mind seeing an option using our the Blue/Purple gradient from our website (varnek-example.co.uk), but also open to non-gradient approaches and other colours..

Overall look: Smart, modern, and distinctive.
Format & Print Specs
Double-sided business card format. (Use a standard size

Must-Haves
Front: Varnek wording or Varnek Group wording with atleast 1 logo also on front “Business Communications | Business Energy.”

Back: Contact + company details and core products.
A design that stands out while remaining professional.

Nice-to-Have Options
A gradient version using our site’s Blue/Purple gradient.
A non-gradient version.
A dual-logo treatment versus a single-logo treatment.

Thanks
Dominic

```html
<!DOCTYPE html>
<html lang="en">
<head>
<meta charset="utf-8">
<title>Varnek Group Business Card</title>
<link rel="stylesheet" href="https://fonts.googleapis.com/css2?family=Montserrat:wght@500;700;800&family=Poppins:wght@600&family=Oswald:wght@600&family=Tinos&display=swap">
<style>
  :root {
    --page: #9a9a9a;
    --card: #ffffff;
    --navy: #1c1566;
    --ink: #222222;
    --heading: #333333;
    --rule: #555555;
    --green: #4caf1a;
    --blue: #1565d8;
    --band-start: #9a1ac9;
    --band-mid: #5a3ab8;
    --band-end: #1a62a6;
  }
  * { margin: 0; padding: 0; box-sizing: border-box; }
  html, body { width: 1200px; height: 1059px; overflow: hidden; background: var(--page); }
  .card {
    position: absolute;
    background: var(--card);
    border-radius: 24px;
    overflow: hidden;
  }
  .card--front { left: 252px; top: 88px; width: 724px; height: 415px; }
  .card--back { left: 252px; top: 566px; width: 712px; height: 407px; }

  .brand { position: absolute; display: flex; flex-direction: column; align-items: center; }
  .brand__dot { width: 100px; height: 100px; border-radius: 50%; }
  .brand__name {
    font-family: "Montserrat", sans-serif;
    font-weight: 800;
    font-size: 47px;
    letter-spacing: 1px;
    color: var(--navy);
    line-height: 1;
    margin-top: 8px;
  }
  .card--front .brand { left: 460px; top: 34px; width: 200px; }
  .card--front .brand__dot { background: var(--green); }
  .card--back .brand { left: 234px; top: 162px; width: 244px; }
  .card--back .brand__dot { width: 120px; height: 120px; background: var(--blue); }

  .person { position: absolute; left: 41px; top: 152px; }
  .person__name {
    font-family: "Montserrat", sans-serif; font-weight: 700;
    font-size: 28px; color: var(--navy); line-height: 1;
  }
  .person__role {
    font-family: "Tinos", serif; font-size: 18px; color: var(--ink);
    margin-top: 12px;
  }
  .divider { position: absolute; left: 41px; top: 237px; width: 635px; height: 1.5px; background: var(--rule); }

  .contacts { position: absolute; left: 40px; top: 256px; list-style: none; }
  .contacts li {
    display: flex; align-items: center; gap: 11px; height: 33.5px;
    font-family: "Montserrat", sans-serif; font-weight: 500; font-size: 19px; color: var(--ink);
  }
  .contacts svg { width: 18px; height: 18px; fill: var(--green); flex: none; }

  .address {
    position: absolute; right: 48px; top: 283px; text-align: right;
    font-family: "Montserrat", sans-serif; font-weight: 500; font-size: 19px;
    line-height: 33px; color: var(--ink);
  }

  .products {
    position: absolute; left: 0; right: 0; bottom: 0; height: 47px;
    background: linear-gradient(90deg, var(--band-start), var(--band-mid) 50%, var(--band-end));
  }
  .products__band {
    position: absolute; left: 0; right: 0; bottom: 0; height: 41px;
    display: flex; align-items: center; justify-content: center; gap: 12px;
    border-top: 3px solid var(--card);
    font-family: "Oswald", sans-serif; font-weight: 600; font-size: 24px;
    color: #fff; letter-spacing: 0.2px; white-space: nowrap;
    background: linear-gradient(90deg, var(--band-start), var(--band-mid) 50%, var(--band-end));
  }

  .group-title {
    position: absolute; left: 0; right: 0; top: 70px; text-align: center;
    font-family: "Poppins", sans-serif; font-weight: 600; font-size: 56px;
    color: var(--heading); line-height: 1;
  }
</style>
</head>
<body>
  <section class="card card--front">
    <div class="brand">
      <div class="brand__dot"></div>
      <div class="brand__name">VARNEK</div>
    </div>

    <div class="person">
      <div class="person__name">Marcus Hale</div>
      <div class="person__role">Owner</div>
    </div>

    <div class="divider"></div>

    <ul class="contacts">
      <li>
        <svg viewBox="0 0 24 24"><path d="M6.6 10.8a15 15 0 0 0 6.6 6.6l2.2-2.2a1 1 0 0 1 1-.25 11.4 11.4 0 0 0 3.6.57 1 1 0 0 1 1 1V20a1 1 0 0 1-1 1A17 17 0 0 1 3 4a1 1 0 0 1 1-1h3.5a1 1 0 0 1 1 1c0 1.25.2 2.45.57 3.6a1 1 0 0 1-.25 1z"/></svg>
        044-000 555 0192
      </li>
      <li>
        <svg viewBox="0 0 24 24"><path d="M2 5h20v14H2z M2 5l10 7 10-7" stroke="#fff" stroke-width="1.5"/></svg>
        info@mail-example.com
      </li>
      <li>
        <svg viewBox="0 0 24 24"><circle cx="12" cy="12" r="10"/><path d="M7 6c2 1 1 3 3 4s0 4 2 5M15 4c-1 2 1 3 3 3M14 20c0-2 2-3 4-2" stroke="#fff" stroke-width="1.6" fill="none"/></svg>
        www.varnek-example.co.uk
      </li>
    </ul>

    <div class="address">
      421, Address line goes here<br>
      45452, Country name
    </div>

    <div class="products__band">
      <span>Business Mobile</span><span>•</span><span>Telephony</span><span>•</span><span>Internet</span><span>•</span><span>Business Energy Solutions</span>
    </div>
  </section>

  <section class="card card--back">
    <h1 class="group-title">Varnek Group</h1>
    <div class="brand">
      <div class="brand__dot"></div>
      <div class="brand__name">VARNEK</div>
    </div>
  </section>
</body>
</html>
```